Copperfinch Menu

I want to re design my menu at our restaurant Copperfinch, the current menu and information about the restaurant is online at www.copperfinch-eatery.example, have attached the logo for Copperfinch as well as the new menu specifications

Menu design Specifications
· Rustic

· Raw

· Unpolished

· Urban

```html
<!DOCTYPE html>
<html lang="en">
<head>
<meta charset="utf-8">
<title>Copperfinch Menu</title>
<link href="https://fonts.googleapis.com/css2?family=Arimo:wght@400;700&display=swap" rel="stylesheet">
<style>
  :root {
    --paper-light: #f6e2d6;
    --paper-mid: #e9c4b0;
    --paper-deep: #d6a48c;
    --edge-dark: #2b1d18;
    --ink: #2a1f1c;
    --glass-top: rgba(120, 72, 52, 0.22);
    --glass-bottom: rgba(70, 40, 30, 0.45);
  }
  html, body {
    margin: 0;
    padding: 0;
    overflow: hidden;
    background: #ffffff;
  }
  .menu {
    position: relative;
    width: 849px;
    height: 1200px;
    overflow: hidden;
    font-family: "Arimo", Arial, sans-serif;
    color: var(--ink);
  }
  .paper-texture {
    position: absolute;
    inset: 0;
    background:
      radial-gradient(ellipse at 30% 25%, var(--paper-light) 0%, transparent 55%),
      radial-gradient(ellipse at 75% 60%, var(--paper-mid) 0%, transparent 60%),
      linear-gradient(160deg, var(--paper-light) 0%, var(--paper-mid) 50%, var(--paper-deep) 100%);
  }
  .edge-band {
    position: absolute;
    left: 0;
    width: 100%;
    background: var(--edge-dark);
  }
  .edge-band--top { top: 0; height: 22px; }
  .edge-band--bottom { bottom: 0; height: 18px; }
  .glass-feature {
    position: absolute;
    left: 436px;
    top: 425px;
    width: 300px;
    height: 760px;
    background: linear-gradient(180deg, var(--glass-top) 0%, var(--glass-bottom) 100%);
    border-radius: 0 0 6px 6px / 0 0 6px 6px;
  }
  .brand-title {
    position: absolute;
    top: 138px;
    left: 0;
    width: 100%;
    text-align: center;
    font-size: 62px;
    font-weight: 700;
    letter-spacing: 3px;
    color: var(--ink);
    margin: 0;
  }
  .brand-small {
    position: absolute;
    top: 282px;
    left: 0;
    width: 100%;
    text-align: center;
    font-size: 13px;
    font-weight: 700;
    letter-spacing: 0.5px;
    color: var(--ink);
  }
  .section {
    position: absolute;
    left: 39px;
    width: 740px;
    font-size: 15.5px;
    line-height: 18.8px;
  }
  .section h2 {
    font-size: 15.5px;
    font-weight: 400;
    margin: 0;
    line-height: 18.8px;
  }
  .item {
    display: flex;
    justify-content: space-between;
    white-space: nowrap;
  }
  .price { text-align: right; }
  .price-pair { display: flex; gap: 8px; }
  .price-pair span { width: 24px; text-align: right; }
  .section--snacks { top: 335px; }
  .section--salads { top: 617px; }
  .section--boards { top: 787px; }
  .section--cheese { top: 1031px; }
</style>
</head>
<body>
<main class="menu">
  <div class="paper-texture" role="img" aria-label="Distressed peach and rose paper texture background"></div>
  <div class="edge-band edge-band--top"></div>
  <div class="edge-band edge-band--bottom"></div>
  <div class="glass-feature" role="img" aria-label="Large silhouette of a wine glass"></div>

  <h1 class="brand-title">COPPERFINCH</h1>
  <div class="brand-small">COPPERFINCH</div>

  <section class="section section--snacks">
    <h2>Snacks</h2>
    <div class="item"><span>Pork crackling</span><span class="price">5</span></div>
    <div class="item"><span>Venison pasties &amp; plum sauce</span><span class="price">12</span></div>
    <div class="item"><span>Lamb Meat balls &amp; pomegranate molasses</span><span class="price">15</span></div>
    <div class="item"><span>Pulled pork &amp; apple slaw Sliders</span><span class="price">12</span></div>
    <div class="item"><span>Cheese fondue &amp; Asparagus</span><span class="price">10</span></div>
    <div class="item"><span>Battered fish fingers &amp; tartare sauce</span><span class="price">9</span></div>
    <div class="item"><span>Hand cut fries &amp; tomato sauce</span><span class="price">7</span></div>
    <div class="item"><span>Salmon &amp; avocado filled Sesame cones</span><span class="price">12</span></div>
    <div class="item"><span>Parmesan, chilli &amp; lemon Skinny fries</span><span class="price">7</span></div>
    <div class="item"><span>Barbequed Chicken tulips</span><span class="price">14</span></div>
    <div class="item"><span>Steamed mussels &amp; tomato salsa</span><span class="price">12</span></div>
    <div class="item"><span>Garlic bread</span><span class="price">6</span></div>
    <div class="item"><span>Crispy lentil balls &amp; roast garlic yoghurt</span><span class="price">8</span></div>
  </section>

  <section class="section section--salads">
    <h2>Salads &amp; sides</h2>
    <div class="item"><span>Warmed Red skinned potatoes with dill &amp; mustard</span><span class="price-pair"><span>6</span><span>9</span></span></div>
    <div class="item"><span>Tomato &amp; mixed beans</span><span class="price-pair"><span>8</span><span>11</span></span></div>
    <div class="item"><span>Char grilled vegetables &amp; halloumi</span><span class="price-pair"><span>7</span><span>10</span></span></div>
    <div class="item"><span>Orzo, broadbean &amp;feta</span><span class="price-pair"><span>7</span><span>10</span></span></div>
    <div class="item"><span>Beetroot, spinach &amp; goats cheese with maple</span><span class="price-pair"><span>8</span><span>11</span></span></div>
    <div class="item"><span>Mixed leaves &amp; citrus emulsion</span><span class="price-pair"><span>6</span><span>9</span></span></div>
    <div class="item"><span>Steamed Broccoli &amp; sesame butter</span><span class="price-pair"><span>6</span><span>9</span></span></div>
  </section>

  <section class="section section--boards">
    <h2>Boards + two sides&nbsp; /&nbsp; for one or two</h2>
    <div class="item"><span>Beef wellington &amp; red wine jus</span><span class="price-pair"><span>36</span><span>69</span></span></div>
    <div class="item"><span>Apricot glazed chicken crown</span><span class="price-pair"><span>34</span><span>65</span></span></div>
    <div class="item"><span>Roast Pork scotch &amp; caramelised apple sauce</span><span class="price-pair"><span>32</span><span>60</span></span></div>
    <div class="item"><span>Pan fried line caught fish &amp; lemon pickle</span><span class="price-pair"><span>35</span><span>67</span></span></div>
    <div class="item"><span>Grilled lamb rack &amp; mint sauce</span><span class="price-pair"><span>38</span><span>72</span></span></div>
    <div class="item"><span>Mixed roast nut loaf &amp; rhubarb marmalade</span><span class="price-pair"><span>28</span><span>58</span></span></div>
    <h2>Sweets</h2>
    <div class="item"><span>Orange pannacotta with earl grey &amp; cardamom syrup</span><span class="price">12</span></div>
    <div class="item"><span>Chocolate terrine, macerated strawberries &amp; macadamia mascarpone</span><span class="price">14</span></div>
    <div class="item"><span>Vanilla bean crème brulee with cranberry &amp; pistachio biscotti</span><span class="price">12</span></div>
    <div class="item"><span>Pavolva roulade, kiwifruit, summer berries &amp; passionfruit cream</span><span class="price">12</span></div>
  </section>

  <section class="section section--cheese">
    <h2>Cheese</h2>
    <div class="item"><span>Ridgeback aged cheddar</span><span class="price">16</span></div>
    <div class="item"><span>Hollow Hill triple Brie</span><span class="price">18</span></div>
    <div class="item"><span>Stillwater Blue</span><span class="price">14</span></div>
    <div class="item"><span>with dried fruit, nuts, fruit paste and wafers</span></div>
  </section>
</main>
</body>
</html>
```